Web design concept for a IT recruitment agency.

Our website addresses two different target groups:
- Customers (companies) wanting to hire new IT talent
- It talent to find a new JOB

We a looking for a visual design concept that either addresses both target groups in one of the following options:
a. target both groups in 1 single splash page.
b. target both groups in 2 different pages one for both groups
c. or any creative third concept you can come up with

Requirements, we want one overall visual concept, that both target groups can relate to.

Trigger words what we want to express:
- passion / drive
- knowhow
- involvement
- professional/yet playful
- engagement

Background, company culture:
We are a recruitment agency with over 15 years of experience, we have no hard-sale culture.
But we emphasize on long term relationships, showing real interest in people and their needs.

Design requirements:
Use logo
Flat contemporary design

Target Market(s)

Industry/Entity Type

Hire

Number of Pages Required

2 page

Requirements
Must have
• We a looking for a visual design concept that either addresses both target groups

```html
<!DOCTYPE html>
<html lang="en">
<head>
<meta charset="utf-8">
<title>Talentrix IT Recruitment</title>
<link href="https://fonts.googleapis.com/css2?family=Open+Sans:wght@400;600;700&display=swap" rel="stylesheet">
<style>
:root{
  --blue:#1e9be0;
  --green:#6cbf3a;
  --orange:#f05a1f;
  --text:#444;
  --heading:#333;
  --muted:#8a8a8a;
  --footer:#2a2a2a;
  --footer-bottom:#1e1e1e;
  --white:#fff;
}
*{box-sizing:border-box;margin:0;padding:0}
html,body{width:702px;height:1200px;overflow:hidden;background:var(--white);font-family:"Open Sans",Arial,sans-serif;color:var(--text)}
.page{width:702px;height:1200px;position:relative}
.container{width:586px;margin:0 auto}

.site-header{height:82px;border-top:3px solid var(--blue);background:var(--white)}
.site-header .container{display:flex;justify-content:space-between;align-items:center;height:79px}
.brand-name{font-size:19px;font-weight:600;color:var(--heading)}
.main-nav{display:flex;gap:20px}
.main-nav a{font-size:8px;font-weight:600;color:#666;text-decoration:none;text-transform:uppercase;padding-bottom:5px}
.main-nav a.active{color:var(--blue);border-bottom:2px solid var(--blue)}

.hero{height:304px;background:linear-gradient(120deg,#7d8c96 0%,#b9c0c4 40%,#8a8f93 70%,#4e5358 100%);display:flex;flex-direction:column;align-items:center;justify-content:center;color:var(--white);text-align:center}
.hero-title{font-size:25px;font-weight:700;letter-spacing:.5px}
.hero-sub{font-size:7px;letter-spacing:1px;text-transform:uppercase;margin:6px 0 14px}
.btn{display:inline-block;background:var(--blue);color:var(--white);font-size:8px;font-weight:600;padding:8px 26px;text-transform:uppercase}

.welcome{text-align:center;padding:24px 0 16px}
.section-title{font-size:15px;font-weight:700;color:var(--heading);text-transform:uppercase}
.welcome p{font-size:7.5px;color:var(--muted);line-height:1.6;margin-top:10px}

.audiences{display:flex;gap:26px}
.audience{flex:1;height:77px;color:var(--white);padding:12px 16px}
.audience.employers{background:var(--green)}
.audience.seekers{background:var(--orange)}
.audience h3{font-size:12px;font-weight:700;text-transform:uppercase;display:flex;align-items:center;gap:8px}
.audience p{font-size:7px;line-height:1.6;margin-top:8px}

.latest{padding-top:30px}
.small-title{font-size:11px;font-weight:700;color:var(--heading);text-transform:uppercase}
.latest-intro{font-size:7px;color:var(--muted);margin:6px 0 12px}
.post-grid{display:flex;gap:14px}
.post{flex:1}
.post-photo{height:96px}
.post h4{font-size:7px;font-weight:700;color:var(--blue);text-transform:uppercase;margin-top:8px}
.post p{font-size:6.5px;color:var(--muted);line-height:1.6;margin-top:4px}

.bottom-row{display:flex;gap:26px;margin-top:44px}
.works{width:280px}
.works-grid{display:grid;grid-template-columns:repeat(3,1fr);gap:4px;margin-top:12px}
.works-grid div{height:78px}
.news{flex:1}
.news-item{display:flex;gap:10px;margin-top:12px}
.news-photo{width:80px;height:72px;flex:none}
.news-item h5{font-size:7.5px;color:var(--blue);font-weight:600}
.news-date{font-size:6.5px;color:#666;margin:4px 0;display:flex;align-items:center;gap:4px}
.news-item p{font-size:6.5px;color:var(--muted);line-height:1.6}

.site-footer{position:absolute;top:1058px;left:0;width:702px;height:142px;background:var(--footer);color:#bbb}
.footer-cols{display:flex;justify-content:space-between;padding-top:16px;height:118px}
.footer-col h6{font-size:7.5px;font-weight:700;color:var(--white);text-transform:uppercase;margin-bottom:8px}
.footer-col p{font-size:6.5px;line-height:1.7}
.contact-line{display:flex;align-items:center;gap:5px;font-size:6.5px;margin-top:3px}
.social{display:flex;gap:6px}
.social span{width:16px;height:16px;border-radius:50%;border:1px solid #999}
.newsletter{width:170px}
.subscribe{display:flex;margin-top:8px}
.subscribe span{flex:1;height:17px;background:var(--white);font-size:6px;color:#aaa;padding:4px 6px}
.subscribe b{background:var(--blue);color:var(--white);font-size:6.5px;padding:4px 8px;font-weight:600}
.footer-bottom{height:24px;background:var(--footer-bottom);font-size:6.5px}
.footer-bottom .container{display:flex;justify-content:space-between;align-items:center;height:24px}

.ph-office{background:linear-gradient(135deg,#c9d3da,#7f8c96)}
.ph-warm{background:linear-gradient(135deg,#d8cbbf,#8e7f73)}
.ph-cool{background:linear-gradient(135deg,#a9b8c4,#4d5c68)}
</style>
</head>
<body>
<div class="page">
  <header class="site-header">
    <div class="container">
      <div class="brand"><span class="brand-name">Talentrix</span></div>
      <nav class="main-nav">
        <a class="active" href="#">Home</a><a href="#">About us</a><a href="#">Services</a><a href="#">Careers</a><a href="#">Testimonials</a><a href="#">Contact us</a><a href="#">Privacy policy</a>
      </nav>
    </div>
  </header>

  <section class="hero" role="img" aria-label="Business team meeting around a table in a bright office">
    <h1 class="hero-title">IT RECRUITMENT AGENCY</h1>
    <p class="hero-sub">We match IT talent with companies for long term success</p>
    <span class="btn">Job search</span>
  </section>

  <div class="container">
    <section class="welcome">
      <h2 class="section-title">Welcome to our company</h2>
      <p>With over fifteen years of experience we connect passionate IT professionals with companies that value them. No hard selling, just<br>genuine interest in people, their ambitions and their needs, building relationships that last for many years to come.</p>
    </section>

    <section class="audiences">
      <div class="audience employers">
        <h3><svg width="16" height="12" viewBox="0 0 16 12"><circle cx="5" cy="3" r="2.5" fill="#fff"/><circle cx="11" cy="3" r="2.5" fill="#fff"/><path d="M0 12c0-4 2-6 5-6s5 2 5 6zM8 12c0-4 1-6 3-6s5 2 5 6z" fill="#fff"/></svg>Employers</h3>
        <p>Find skilled IT talent that fits your team and culture.<br>We take time to understand your goals. Read more</p>
      </div>
      <div class="audience seekers">
        <h3><svg width="14" height="12" viewBox="0 0 14 12"><rect x="0" y="3" width="14" height="9" fill="#fff"/><rect x="4.5" y="0" width="5" height="4" fill="none" stroke="#fff" stroke-width="1.5"/></svg>Job seekers</h3>
        <p>Discover roles that match your skills and your drive.<br>We guide you every step of the way. Read more</p>
      </div>
    </section>

    <section class="latest">
      <h3 class="small-title">Latest posts</h3>
      <p class="latest-intro">Fresh insights on the IT job market, hiring trends and career advice from our consultants and partners.</p>
      <div class="post-grid">
        <article class="post"><div class="post-photo ph-office" role="img" aria-label="Smiling professional woman in an office"></div><h4>Directions of passages</h4><p>How to prepare for your next technical interview with confidence.</p></article>
        <article class="post"><div class="post-photo ph-cool" role="img" aria-label="Woman working on a laptop"></div><h4>Directions of passages</h4><p>Why company culture matters when choosing a new role.</p></article>
        <article class="post"><div class="post-photo ph-warm" role="img" aria-label="Hands on a laptop keyboard"></div><h4>Directions of passages</h4><p>Five skills every developer should grow this year.</p></article>
        <article class="post"><div class="post-photo ph-cool" role="img" aria-label="Businessman in a suit"></div><h4>Directions of passages</h4><p>Building long term teams through honest recruitment.</p></article>
      </div>
    </section>

    <section class="bottom-row">
      <div class="works">
        <h3 class="small-title">Our works</h3>
        <div class="works-grid">
          <div class="ph-office" role="img" aria-label="Team discussion"></div>
          <div class="ph-warm" role="img" aria-label="Handshake meeting"></div>
          <div class="ph-cool" role="img" aria-label="Office workers"></div>
          <div class="ph-warm" role="img" aria-label="Colleagues at a desk"></div>
          <div class="ph-office" role="img" aria-label="Group of professionals"></div>
          <div class="ph-cool" role="img" aria-label="Modern office building"></div>
        </div>
      </div>
      <div class="news">
        <h3 class="small-title">News &amp; updates</h3>
        <div class="news-item">
          <div class="news-photo ph-cool" role="img" aria-label="Business meeting"></div>
          <div><h5>New Developer Vacancies</h5><div class="news-date"><svg width="7" height="7" viewBox="0 0 8 8"><circle cx="4" cy="4" r="3.4" fill="none" stroke="#666"/><path d="M4 2v2h2" stroke="#666" fill="none"/></svg>10:00 pm · 18 march</div><p>Several new developer positions opened this week with partner companies across the region, apply today.</p></div>
        </div>
        <div class="news-item">
          <div class="news-photo ph-office" role="img" aria-label="Colleagues reviewing documents"></div>
          <div><h5>New Developer Vacancies</h5><div class="news-date"><svg width="7" height="7" viewBox="0 0 8 8"><circle cx="4" cy="4" r="3.4" fill="none" stroke="#666"/><path d="M4 2v2h2" stroke="#666" fill="none"/></svg>10:00 pm · 12 march</div><p>Our team joined the regional tech fair to meet talented engineers and hiring managers.</p></div>
        </div>
      </div>
    </section>
  </div>

  <footer class="site-footer">
    <div class="container footer-cols">
      <div class="footer-col">
        <h6>Contact us</h6>
        <p>120 Market Street, Suite 4<br>Riverside, 2045 Northland</p>
        <div class="contact-line"><svg width="7" height="7" viewBox="0 0 8 8"><path d="M1 1l2 0 1 2-1 1a4 4 0 0 0 2 2l1-1 2 1v2c-4 0-7-3-7-7z" fill="#bbb"/></svg>+00 1234 567</div>
        <div class="contact-line"><svg width="8" height="6" viewBox="0 0 8 6"><rect x=".5" y=".5" width="7" height="5" fill="none" stroke="#bbb"/><path d="M.5.5l3.5 3 3.5-3" fill="none" stroke="#bbb"/></svg>hello@talentrix-hiring.example</div>
      </div>
      <div class="footer-col">
        <h6>Follow us</h6>
        <div class="social"><span></span><span></span><span></span><span></span><span></span></div>
      </div>
      <div class="footer-col newsletter">
        <h6>Newsletter</h6>
        <p>Sign up to receive the latest vacancies and news straight in your inbox.</p>
        <div class="subscribe"><span>Enter your email address</span><b>Sign up</b></div>
      </div>
    </div>
    <div class="footer-bottom"><div class="container"><span>Copyright © 2024 Talentrix IT recruitment agency. All rights reserved.</span><span>Top</span></div></div>
  </footer>
</div>
</body>
</html>
```